Electrical contractor in San Diego county since 1988

Provide a company name/ logo for business cards and forms. Newer and more modern old card is attached. Color preference is black and orange. Simple and streamlined nothing too busy. I have also attached a card that represents the simplicity of what we are looking for.

Contractor

```html
<!DOCTYPE html>
<html lang="en">
<head>
<meta charset="utf-8">
<title>K.M. Electric INC. – Business Cards</title>
<link rel="stylesheet" href="https://fonts.googleapis.com/css2?family=Montserrat:wght@400;500;600&display=swap">
<style>
  :root {
    --orange: #e8793a;
    --ink: #1f1f1f;
    --paper: #ffffff;
    --backdrop: #e9e6df;
  }
  * { box-sizing: border-box; margin: 0; padding: 0; }
  html, body {
    width: 1200px;
    height: 800px;
    overflow: hidden;
  }
  body {
    background: var(--backdrop);
    font-family: "Montserrat", sans-serif;
    color: var(--ink);
  }
  .canvas {
    width: 1200px;
    height: 800px;
    display: flex;
    flex-direction: column;
    align-items: center;
    justify-content: center;
    gap: 40px;
  }
  .card {
    position: relative;
    width: 600px;
    height: 343px;
    background: var(--paper);
    border-top: 14px solid var(--orange);
    border-bottom: 14px solid var(--orange);
    box-shadow: 0 6px 18px rgba(0,0,0,0.12);
  }
  .lockup {
    position: absolute;
    left: 0;
    right: 0;
    top: 62px;
    text-align: center;
  }
  .card--back .lockup { top: 42px; }
  .lockup__mark {
    display: block;
    width: 54px;
    height: 54px;
    margin: 0 auto 14px;
    border-radius: 50%;
    background: var(--orange);
  }
  .lockup__license {
    font-size: 9px;
    font-weight: 500;
    letter-spacing: 0.3px;
    margin-bottom: 5px;
  }
  .lockup__name {
    font-size: 19px;
    font-weight: 500;
    letter-spacing: 0.3px;
    margin-bottom: 8px;
  }
  .lockup__tagline {
    font-size: 10px;
    font-weight: 500;
  }
  .contact {
    position: absolute;
    display: flex;
    align-items: flex-start;
    gap: 9px;
    font-size: 10px;
    font-weight: 500;
    line-height: 1.35;
    letter-spacing: 0.3px;
  }
  .contact svg {
    flex: none;
    width: 11px;
    height: 11px;
    margin-top: 2px;
    fill: var(--orange);
  }
  .contact--phone { right: 48px; top: 176px; }
  .contact--address { left: 250px; top: 218px; }
  .contact--person { left: 34px; bottom: 26px; }
  .contact__name { text-transform: uppercase; }
  .contact__title { padding-left: 6px; }
</style>
</head>
<body>
<main class="canvas">

  <section class="card card--front">
    <div class="lockup">
      <span class="lockup__mark"></span>
      <p class="lockup__license">Lic. 700312</p>
      <h1 class="lockup__name">K.M. Electric INC.</h1>
      <p class="lockup__tagline">Commercial - New &amp; Remodel</p>
    </div>
  </section>

  <section class="card card--back">
    <div class="lockup">
      <span class="lockup__mark"></span>
      <p class="lockup__license">Lic. 700312</p>
      <h2 class="lockup__name">K.M. Electric INC.</h2>
      <p class="lockup__tagline">Commercial - New &amp; Remodel</p>
    </div>

    <div class="contact contact--phone">
      <svg viewBox="0 0 24 24" aria-hidden="true"><path d="M6.6 10.8a15.1 15.1 0 0 0 6.6 6.6l2.2-2.2a1 1 0 0 1 1-.25 11.4 11.4 0 0 0 3.6.57 1 1 0 0 1 1 1V20a1 1 0 0 1-1 1A17 17 0 0 1 3 4a1 1 0 0 1 1-1h3.5a1 1 0 0 1 1 1c0 1.25.2 2.45.57 3.57a1 1 0 0 1-.25 1z"/></svg>
      <div>
        <p>(619) 555 - 0142</p>
        <p>FAX: 555 - 0187</p>
      </div>
    </div>

    <div class="contact contact--address">
      <svg viewBox="0 0 24 24" aria-hidden="true"><path d="M12 2a7 7 0 0 0-7 7c0 5.25 7 13 7 13s7-7.75 7-13a7 7 0 0 0-7-7zm0 9.5A2.5 2.5 0 1 1 12 6.5a2.5 2.5 0 0 1 0 5z"/></svg>
      <div>
        <p>P.O. Box 4417</p>
        <p>Alpine, CA 91901 - 0417</p>
      </div>
    </div>

    <div class="contact contact--person">
      <svg viewBox="0 0 24 24" aria-hidden="true"><circle cx="12" cy="7" r="5"/><path d="M2 22c0-5 4.5-8 10-8s10 3 10 8z"/></svg>
      <div>
        <p class="contact__name">Dana Whitfield</p>
        <p class="contact__title">President</p>
      </div>
    </div>
  </section>

</main>
</body>
</html>
```